Google Form Graphic to suit our Brand and industry

Create a graphic / image for us to put at the top of our client enquiry google form.
The image will be a section of an architectural home with our branding over the top. Preferably translucent.
The image must suit the shape of the google forms image, which is an elongated rectangle
#003d5d - brand colour

Target Market(s)

residential home owners, high end architectural homes

Industry/Entity Type

Residential construction

Colors
0054AA
0677BA
7BADD7
CADEEF
E8F1F8

Requirements
Must have
• our branding and a photo of an architectural home in the background

```html
<!DOCTYPE html>
<html lang="en">
<head>
<meta charset="utf-8">
<title>New Client Enquiry Form</title>
<link rel="stylesheet" href="https://fonts.googleapis.com/css2?family=Roboto:wght@400;500&display=swap">
<style>
  :root {
    --page-bg: #f6efdf;
    --brand-navy: #003d5d;
    --card-bg: #ffffff;
    --card-border: #dedcd6;
    --text-main: #202124;
    --text-muted: #70757a;
    --accent-blue: #4285f4;
    --title-rule: #8a7350;
    --required-red: #d93025;
    --tab-gold: #e3b95f;
    --divider: #d4d0c6;
    --photo-light: #f4f4f4;
    --photo-mid: #d2d4d6;
  }
  * { box-sizing: border-box; margin: 0; padding: 0; }
  html, body { width: 862px; height: 1200px; overflow: hidden; }
  body {
    background: var(--page-bg);
    font-family: "Roboto", Arial, sans-serif;
    color: var(--text-main);
    position: relative;
  }
  .header-banner {
    position: absolute; left: 31px; top: 12px; width: 804px; height: 200px;
    border-radius: 9px; overflow: hidden;
  }
  .header-banner__photo {
    position: absolute; inset: 0;
    background: linear-gradient(100deg, var(--photo-light) 30%, var(--photo-mid) 60%, var(--photo-light) 100%);
  }
  .header-banner__shape { position: absolute; inset: 0; }
  .brand-name {
    position: absolute; left: 290px; top: 74px;
    font-size: 50px; font-weight: 400; letter-spacing: 1px;
    color: var(--brand-navy); line-height: 1;
  }
  .card {
    position: absolute; left: 34px; width: 791px;
    background: var(--card-bg); border: 1px solid var(--card-border);
    border-radius: 8px; overflow: hidden;
  }
  .card--title { top: 272px; height: 171px; border-top-left-radius: 0; border-top-right-radius: 0; }
  .form-title {
    position: absolute; left: 25px; top: 24px; font-size: 32px; font-weight: 400;
  }
  .form-title__rule {
    position: absolute; left: 25px; top: 70px; width: 654px; height: 1px; background: var(--title-rule);
  }
  .title-tools { position: absolute; right: 26px; top: 28px; display: flex; gap: 30px; }
  .format-bar {
    position: absolute; left: 40px; top: 82px; display: flex; gap: 22px; align-items: center;
  }
  .format-bar span { font-size: 17px; color: #444; width: 20px; text-align: center; }
  .form-description { position: absolute; left: 25px; top: 126px; font-size: 14px; }
  .card--question { height: 141px; }
  .card--active::before {
    content: ""; position: absolute; left: 0; top: 0; bottom: 0; width: 6px; background: var(--accent-blue);
  }
  .question-label { position: absolute; left: 25px; top: 28px; font-size: 16px; }
  .card--active .question-label { left: 33px; }
  .required-mark { color: var(--required-red); margin-left: 8px; }
  .answer-placeholder {
    position: absolute; left: 25px; top: 74px; width: 371px; padding-bottom: 4px;
    font-size: 13px; color: var(--text-muted); border-bottom: 1px dotted #9aa0a6;
  }
  .section-nav {
    position: absolute; left: 33px; top: 1086px; font-size: 13px; color: #3c4043;
    display: flex; gap: 18px; align-items: center;
  }
  .section-nav__select { display: flex; gap: 160px; align-items: center; }
  .section-rail { position: absolute; left: 835px; top: 1088px; width: 1px; height: 112px; background: var(--divider); }
  .section-tab {
    position: absolute; left: 33px; top: 1165px; width: 124px; height: 44px;
    background: var(--tab-gold); border-radius: 8px 8px 0 0;
    font-size: 12.5px; padding: 11px 0 0 17px; color: #2b2b2b;
  }
</style>
</head>
<body>
  <header class="header-banner">
    <div class="header-banner__photo" role="img" aria-label="Softly faded photograph of a modern two-storey architectural home with large glass windows"></div>
    <svg class="header-banner__shape" viewBox="0 0 804 200" aria-hidden="true">
      <polygon points="0,0 286,0 212,100 286,200 0,200" fill="var(--brand-navy)"/>
    </svg>
    <div class="brand-name">NORVA BUILD</div>
  </header>

  <section class="card card--title">
    <h1 class="form-title">New Client Enquiry Form</h1>
    <div class="form-title__rule"></div>
    <div class="title-tools" aria-hidden="true">
      <svg width="14" height="18" viewBox="0 0 14 18"><path d="M3 2l4 4 4-4M3 16l4-4 4 4" stroke="#5f6368" stroke-width="1.6" fill="none"/></svg>
      <svg width="4" height="18" viewBox="0 0 4 18"><circle cx="2" cy="2" r="1.8" fill="#5f6368"/><circle cx="2" cy="9" r="1.8" fill="#5f6368"/><circle cx="2" cy="16" r="1.8" fill="#5f6368"/></svg>
    </div>
    <div class="format-bar" aria-hidden="true">
      <span style="font-weight:500">B</span>
      <span style="font-style:italic">I</span>
      <span style="text-decoration:underline">U</span>
      <svg width="20" height="12" viewBox="0 0 20 12"><rect x="1" y="2" width="10" height="8" rx="4" fill="none" stroke="#444" stroke-width="1.6"/><rect x="9" y="2" width="10" height="8" rx="4" fill="none" stroke="#444" stroke-width="1.6"/></svg>
      <svg width="18" height="18" viewBox="0 0 18 18"><path d="M3 3h12M9 3v13M3 15L15 5" stroke="#444" stroke-width="1.6" fill="none"/></svg>
    </div>
    <p class="form-description">We would love to hear your thoughts or feedback on how we can improve your experience!</p>
  </section>

  <section class="card card--question card--active" style="top:458px">
    <p class="question-label">Firstly, how did you hear about us?<span class="required-mark">*</span></p>
    <div class="answer-placeholder">Short answer text</div>
  </section>

  <section class="card card--question" style="top:614px">
    <p class="question-label">Name</p>
    <div class="answer-placeholder">Short answer text</div>
  </section>

  <section class="card card--question" style="top:769px">
    <p class="question-label">Phone</p>
    <div class="answer-placeholder">Short answer text</div>
  </section>

  <section class="card card--question" style="top:924px">
    <p class="question-label">Email</p>
    <div class="answer-placeholder">Short answer text</div>
  </section>

  <div class="section-nav">
    <span>After section 1</span>
    <span class="section-nav__select">Continue to next section
      <svg width="10" height="6" viewBox="0 0 10 6"><path d="M0 0h10L5 6z" fill="#5f6368"/></svg>
    </span>
  </div>
  <div class="section-rail"></div>
  <div class="section-tab">Section 2 of 4</div>
</body>
</html>
```